Super elegant, crisp & clean Business card design required

We recently upgraded our branding - which is on our website - tavorelstudio.com

I would like a simple, yet elegant, clean business card design please.

The font of my logo is Cinzel - and because of the natural colour - it's best to have this on a black background.

I would like to have the back of the business card - with simply my logo.

PLEASE DO NOT SUBMIT A COMPLICATED / UNCLEAN DESIGN

Industry/Entity Type

Business

Contact Information for Business Card

Dalvik Ostrander Photography

Font styles to use
Other font styles liked:
• Cinzel

Requirements
Must have
• A backpage with nothing but my logo
• Simple design - stands out
Should not have
• Colour that dont align with my logo
• Over complicated '/ non symmetrical design

```html
<!DOCTYPE html>
<html lang="en">
<head>
<meta charset="utf-8">
<title>Dalvik Ostrander Photography – Business Card</title>
<link rel="stylesheet" href="https://fonts.googleapis.com/css2?family=Cinzel:wght@400&display=swap">
<style>
  :root {
    --card-black: #0a0c0c;
    --brand-gold: #7a7550;
    --text-white: #f4f4f0;
  }
  * { margin: 0; padding: 0; box-sizing: border-box; }
  html, body {
    width: 921px;
    height: 1200px;
    overflow: hidden;
    background: var(--card-black);
  }
  .card {
    position: relative;
    width: 921px;
    height: 1200px;
    background: var(--card-black);
    font-family: "Cinzel", serif;
    font-weight: 400;
  }

  /* Brand block */
  .brand-mark {
    position: absolute;
    left: 311px;
    top: 74px;
    width: 300px;
    height: 300px;
  }
  .brand-name {
    position: absolute;
    left: 0;
    width: 921px;
    top: 438px;
    text-align: center;
    color: var(--brand-gold);
    font-size: 66px;
    line-height: 1;
  }
  .brand-tagline {
    position: absolute;
    left: 0;
    width: 921px;
    top: 530px;
    text-align: center;
    color: var(--brand-gold);
    font-size: 31px;
    line-height: 1;
    letter-spacing: 0.95em;
    padding-left: 0.95em;
    text-transform: uppercase;
  }

  /* Contact block */
  .contact-heading {
    position: absolute;
    left: 60px;
    top: 732px;
    color: var(--text-white);
    font-size: 40px;
    line-height: 1;
  }
  .contact-list { list-style: none; }
  .contact-item {
    position: absolute;
    left: 60px;
    display: flex;
    align-items: center;
    color: var(--text-white);
    text-transform: uppercase;
    line-height: 1;
  }
  .contact-icon {
    width: 60px;
    height: 56px;
    margin-right: 86px;
    flex: none;
    fill: none;
    stroke: var(--brand-gold);
  }
  .contact-item .contact-text { margin-left: -58px; }
  .contact-web   { top: 810px; font-size: 39px; }
  .contact-email { top: 884px; font-size: 35px; }
  .contact-phone { top: 956px; font-size: 44px; }
  .contact-social{ top: 1036px; font-size: 39px; }
</style>
</head>
<body>
<main class="card">

  <svg class="brand-mark" viewBox="0 0 300 300" aria-hidden="true">
    <circle cx="150" cy="150" r="140" fill="none" stroke="var(--brand-gold)" stroke-width="3"/>
  </svg>
  <h1 class="brand-name">Dalvik Ostrander</h1>
  <p class="brand-tagline">Photography</p>

  <h2 class="contact-heading">Dalvik Ostrander Photography</h2>

  <ul class="contact-list">
    <li class="contact-item contact-web">
      <svg class="contact-icon" viewBox="0 0 60 56" aria-hidden="true">
        <circle cx="26" cy="26" r="22" stroke-width="5"/>
        <ellipse cx="26" cy="26" rx="9" ry="22" stroke-width="4"/>
        <line x1="4" y1="26" x2="48" y2="26" stroke-width="4"/>
        <path d="M34 30 L56 42 L47 45 L53 54 L48 56 L42 48 L36 53 Z" fill="var(--brand-gold)" stroke="var(--card-black)" stroke-width="2"/>
      </svg>
      <span class="contact-text">tavorelstudio.com</span>
    </li>
    <li class="contact-item contact-email">
      <svg class="contact-icon" viewBox="0 0 60 56" aria-hidden="true">
        <rect x="3" y="8" width="54" height="40" stroke-width="5"/>
        <path d="M3 8 L30 32 L57 8 M3 48 L23 27 M57 48 L37 27" stroke-width="4"/>
      </svg>
      <span class="contact-text">studio@tavorelstudio.com</span>
    </li>
    <li class="contact-item contact-phone">
      <svg class="contact-icon" viewBox="0 0 60 56" aria-hidden="true">
        <path d="M8 4 L18 2 L24 16 L17 22 C21 32 27 38 36 43 L42 36 L56 42 L54 52 C30 54 6 32 8 4 Z" fill="var(--brand-gold)" stroke="none"/>
      </svg>
      <span class="contact-text">07700 900418</span>
    </li>
    <li class="contact-item contact-social">
      <svg class="contact-icon" viewBox="0 0 60 56" aria-hidden="true">
        <rect x="2" y="0" width="56" height="56" rx="4" fill="var(--brand-gold)" stroke="none"/>
      </svg>
      <span class="contact-text">tavorelstudio</span>
    </li>
  </ul>

</main>
</body>
</html>
```